Business Image

I have recently had a new company logo made up and require some new business cards to go with it.

Target Market(s)

Developers & high worth clients.

Industry/Entity Type

Business

Contact Information for Business Card

The business is in the construction/management industry. It needs to be classy but have a industrial feel. I would like the business card to be a elegant presentation in itself.

Requirements
Must have
• Current logo & company name. Colouring needs to be the same as the current design also.
Nice to have
• A few different designs & presentations of single and double sided business cards.

```html
<!DOCTYPE html>
<html lang="en">
<head>
<meta charset="utf-8">
<title>Ironvale Build Group – Business Card</title>
<link rel="stylesheet" href="https://fonts.googleapis.com/css2?family=Arimo:wght@700&family=Open+Sans:wght@400&family=Tinos:wght@400;700&display=swap">
<style>
  :root {
    --stage: #404040;
    --card: #ffffff;
    --brand-blue: #2a6ea8;
    --back-blue: #2f72ad;
    --steel-grey: #6d6e70;
    --ink: #2b2b2b;
    --white: #ffffff;
  }
  * { box-sizing: border-box; margin: 0; padding: 0; }
  html, body { width: 1200px; height: 900px; overflow: hidden; }
  body { background: var(--stage); position: relative; font-family: "Open Sans", Arial, sans-serif; }

  .card { position: absolute; top: 306px; width: 440px; height: 271px; overflow: hidden; }
  .card--front { left: 149px; background: var(--card); }
  .card--back { left: 608px; background: var(--back-blue); }

  .front__tab { position: absolute; left: 0; top: 26px; }
  .holder { position: absolute; left: 36px; top: 31px; }
  .holder__name { font-family: "Tinos", "Times New Roman", serif; font-size: 15.5px; color: var(--brand-blue); letter-spacing: 0.3px; line-height: 18px; }
  .holder__role { font-size: 11.5px; color: var(--ink); line-height: 15px; }

  .brand-mark { position: absolute; left: 282px; top: 40px; width: 52px; height: 52px; background: var(--brand-blue); }
  .brand { position: absolute; right: 26px; top: 128px; text-align: right; color: var(--brand-blue); font-family: "Tinos", "Times New Roman", serif; font-weight: 700; }
  .brand__name { font-size: 38px; line-height: 38px; letter-spacing: 1px; }
  .brand__sub { font-size: 12.5px; letter-spacing: 3.4px; line-height: 18px; margin-right: -3px; }

  .contacts { position: absolute; left: 28px; top: 177px; list-style: none; }
  .contacts li { display: flex; align-items: center; gap: 7px; font-size: 11.5px; color: var(--ink); line-height: 15.8px; }
  .contacts svg { width: 9px; height: 9px; fill: var(--brand-blue); flex: none; }

  .address { position: absolute; right: 25px; top: 208px; text-align: right; font-size: 11.5px; line-height: 15.8px; color: var(--ink); font-style: normal; }

  .front__bands { position: absolute; left: 0; bottom: 0; }

  .back__texture { position: absolute; inset: 0; background: linear-gradient(135deg, #3277b2, #2b6ca6); }
  .back__brand { position: absolute; left: 0; right: 0; top: 100px; text-align: center; color: var(--white); }
  .back__name { font-family: "Tinos", "Times New Roman", serif; font-weight: 700; font-size: 45px; line-height: 46px; letter-spacing: 1px; }
  .back__sub { font-family: "Tinos", "Times New Roman", serif; font-weight: 700; font-size: 14.5px; letter-spacing: 3.6px; line-height: 20px; }
</style>
</head>
<body>
  <section class="card card--front" aria-label="Business card front">
    <svg class="front__tab" width="30" height="37" viewBox="0 0 30 37" aria-hidden="true">
      <polygon points="0,0 14,0 10,37 0,37" fill="#6d6e70"/>
      <polygon points="14,0 28,0 28,37 10,37" fill="#2a6ea8"/>
    </svg>
    <div class="holder">
      <p class="holder__name">DANIEL HARTLEY</p>
      <p class="holder__role">Managing Director</p>
    </div>

    <div class="brand-mark" aria-hidden="true"></div>
    <div class="brand">
      <p class="brand__name">IRONVALE</p>
      <p class="brand__sub">BUILD GROUP</p>
    </div>

    <ul class="contacts">
      <li><svg viewBox="0 0 10 10"><rect x="2.5" y="0" width="5" height="10" rx="1"/></svg>044-555 010 234</li>
      <li><svg viewBox="0 0 10 10"><path d="M0 3 Q5 0 10 3 L10 4.5 L7.5 4.5 L7.5 3.5 L2.5 3.5 L2.5 4.5 L0 4.5Z M2 5 L8 5 L9.5 10 L0.5 10Z"/></svg>044-555 010 235</li>
      <li><svg viewBox="0 0 10 10"><path d="M0 2 H10 V8 H0Z M0.8 2.6 L5 5.8 L9.2 2.6" stroke="#fff" stroke-width="0.8"/></svg>info@ironvalebuild.com</li>
      <li><svg viewBox="0 0 10 10"><circle cx="5" cy="5" r="5"/></svg>www.ironvalebuild.com</li>
    </ul>

    <address class="address">48 Foundry Lane, Eastgate<br>Northshire, 204518.</address>

    <svg class="front__bands" width="440" height="16" viewBox="0 0 440 16" aria-hidden="true">
      <polygon points="0,2 218,2 210,15 0,15" fill="#6d6e70"/>
      <polygon points="224,0 440,0 440,15 208,15" fill="#2a6ea8"/>
    </svg>
  </section>

  <section class="card card--back" aria-label="Business card back">
    <div class="back__texture" role="img" aria-label="Faint repeating brand texture in blue tones"></div>
    <div class="back__brand">
      <p class="back__name">IRONVALE</p>
      <p class="back__sub">BUILD GROUP</p>
    </div>
  </section>
</body>
</html>
```